Tolvene Hub Redesign

tolvenehub.com is one of our old, high-traffic multilingual site.

its interface is very old, so we want to redesign it to give a modern, attractive design, with comfortable colors and layout.

beside the current content of the main page we want to add two places for dynamic banners.

The site has an App in iOS and Android, we want an ad in a noticeable place for it.

this ad will be permanent.

the site now has 12 languages, but we may add new languages soon, so design must consider this.

redesign of two internal pages also required:
- the main listing page, example: http://www.tolvenehub.example/en/cat/252
- the article view page: http://www.tolvenehub.example/en/10323

Reason: want to receive more designs ...

```html
<!DOCTYPE html>
<html lang="en">
<head>
<meta charset="utf-8">
<title>Tolvene Hub – Home</title>
<link rel="stylesheet" href="https://fonts.googleapis.com/css2?family=Open+Sans:wght@400;600;700&family=Roboto+Condensed:wght@400&display=swap">
<style>
:root{
  --sky-top:#2f8fd6;
  --sky-mid:#7cc0ee;
  --sky-low:#c9e6f8;
  --navy:#0a5a8c;
  --navy-dark:#074a75;
  --link:#0d6aa6;
  --text:#4f5a63;
  --muted:#8a969f;
  --panel:#eef7fd;
  --panel-line:#cfe6f6;
  --white:#ffffff;
  --rule:#c4d9e8;
}
*{box-sizing:border-box;margin:0;padding:0}
html,body{width:900px;height:1200px;overflow:hidden}
body{
  position:relative;
  font-family:"Open Sans",Arial,sans-serif;
  color:var(--text);
  background:linear-gradient(180deg,var(--sky-top) 0,var(--sky-mid) 180px,var(--sky-low) 320px,#d6ecfa 700px,#4aa8ea 1200px);
}
.abs{position:absolute}

/* top strip */
.top-tab{background:var(--white);height:32px;top:0;display:flex;align-items:center;font-size:11px;color:#666;box-shadow:0 1px 3px rgba(0,0,0,.15)}
.social-tab{left:28px;width:270px;border-radius:0 0 12px 12px;padding-left:11px;gap:10px}
.social-tab .sep{width:1px;height:16px;background:#ddd}
.social-tab .net{color:#333;font-weight:600}
.social-tab .net.alt{color:var(--link);font-weight:400}
.lang-tab{left:270px;width:165px;border-radius:0 0 14px 0;padding-left:19px;gap:10px;background:#f7f9fb}
.lang-tab .current{color:var(--link);display:flex;align-items:center;gap:6px}
.lang-tab .current::after{content:"";border:5px solid transparent;border-top:6px solid #888;margin-top:5px}
.date-tab{left:655px;width:235px;border-radius:0 0 0 14px;padding-left:26px;color:#333;font-size:11.5px}

/* brand */
.brand{left:18px;top:125px;display:flex;align-items:center;gap:10px;font-size:38px;font-weight:600;color:var(--navy);letter-spacing:-.5px}
.brand .dot{width:16px;height:16px;border-radius:50%;background:var(--navy)}
.skyline{left:300px;top:78px;width:500px;height:140px;border-radius:60px 60px 0 0;background:radial-gradient(ellipse at 50% 80%,rgba(255,255,255,.85),rgba(255,255,255,.35) 60%,rgba(255,255,255,0) 80%)}

/* page sheet */
.sheet{left:15px;top:240px;width:870px;height:960px;background:linear-gradient(180deg,#eaf5fd 0,#f3f9fe 120px,#eaf4fb 700px,#d2e9f8 960px)}

/* nav */
.main-nav{left:33px;top:219px;width:828px;height:48px;background:linear-gradient(#fff,#eef1f4);border-radius:8px;box-shadow:0 2px 4px rgba(0,0,0,.15);display:flex;align-items:center;padding-left:8px}
.main-nav a{color:var(--link);text-decoration:none;font-size:13px;padding:0 15px;border-right:1px solid #d9dde1;line-height:22px}
.main-nav a:last-child{border:0}
.main-nav a.active{text-decoration:underline}
.search{left:210px;top:262px;width:480px;height:40px;background:var(--navy);border-radius:0 0 40px 40px;border:3px solid var(--white);border-top:0;display:flex;align-items:center;padding-left:27px;color:#fff;font-size:13.5px}
.search .adv{position:absolute;right:6px;top:4px;height:29px;width:170px;background:linear-gradient(#fff,#dce9f3);border-radius:0 0 30px 4px;display:flex;align-items:center;gap:7px;padding-left:20px;color:var(--navy);font-weight:600;font-size:13.5px}

/* intro */
.box{background:var(--white);border:1px solid var(--rule);border-radius:8px;overflow:hidden}
.box-head{background:var(--navy);color:#fff;font-weight:600;text-transform:uppercase}
.intro{left:33px;top:326px;width:828px;height:156px}
.intro .box-head{height:30px;font-size:17.5px;padding:3px 16px}
.intro p{font-size:10.8px;line-height:16.5px;color:var(--link);padding:0 16px;margin-top:11px}
.intro p + p{margin-top:15px}
.intro .more{color:var(--navy);font-weight:700;font-style:italic;text-decoration:underline;margin-left:5px}

/* tabs */
.topics{left:33px;top:509px;width:548px;height:457px;background:var(--panel);border:1px solid var(--panel-line);border-radius:8px}
.tabs{position:absolute;left:2px;top:0;display:flex;gap:4px}
.tab{width:88px;height:41px;background:#d9ecf9;border-radius:6px 6px 0 0;color:var(--link);font-size:11px;line-height:15px;text-align:center;display:flex;align-items:center;justify-content:center}
.tab.active{background:var(--navy);color:#fff}
.tab-body{position:absolute;left:6px;top:42px;width:532px;height:413px;background:#f6fbfe;border:1px solid var(--panel-line);border-radius:0 0 6px 6px}
.topic-list{list-style:none;margin:10px 11px 0 11px}
.topic-list li{height:37.3px;border-bottom:1px dashed #c5dced;display:flex;align-items:center;gap:12px;padding-left:8px;font-size:13px;color:#555}
.topic-list li::before{content:"";width:20px;height:20px;border-radius:50%;background:radial-gradient(circle at 40% 35%,#fff,#dfe8ee)}
.topic-list li.current{background:#d3eafa;color:var(--navy)}
.topic-list li.current::before{background:var(--navy)}
.btn{position:absolute;left:202px;top:363px;width:126px;height:34px;background:var(--navy);color:#fff;font-weight:700;font-size:15px;border-radius:10px;display:flex;align-items:center;justify-content:center}

/* new fatwas */
.new-fatwas{left:600px;top:509px;width:261px;height:458px;background:var(--white);border:1px solid var(--rule);border-radius:8px;padding:5px}
.new-fatwas .box-head{height:30px;font-size:14.5px;padding:5px 9px;border-radius:6px 6px 0 0}
.fatwa{height:69px;border-bottom:1px dashed #c5dced;background:#f4f9fd;font-size:12px;line-height:17.3px;color:var(--muted);padding:6px 10px}
.fatwa.active{color:var(--link);background:#fff}

/* lower columns */
.col{top:993px;width:272px;height:220px;background:#d6ebf9;border-radius:8px;padding:8px}
.col-in{background:#f3f9fe;height:100%;border-radius:6px;padding:0 8px}
.col h2{font-family:"Roboto Condensed","Arial Narrow",sans-serif;font-weight:400;font-size:25px;color:var(--navy);padding:13px 8px 8px}
.col ul{list-style:none}
.col li{font-size:13px;color:#555;line-height:25.3px;border-bottom:1px dashed #c5dced;padding-left:10px}
.col li.linked{color:var(--link);text-decoration:underline}
</style>
</head>
<body>
  <div class="abs sheet"></div>

  <div class="abs top-tab social-tab">
    <span>Follow Up</span><span class="sep"></span>
    <span class="net">Chirper</span><span class="sep"></span>
    <span class="net alt">Facefeed</span>
  </div>
  <div class="abs top-tab lang-tab"><span>Language</span><span style="width:1px;height:16px;background:#ddd"></span><span class="current">English</span></div>
  <div class="abs top-tab date-tab">Fri 27 DhH 1434 - 1 November 2013</div>

  <div class="abs brand"><span class="dot"></span>Tolvene Hub</div>
  <div class="abs skyline" role="img" aria-label="Pale white skyline of domes and minarets fading into the sky"></div>

  <nav class="abs main-nav">
    <a class="active" href="#">Home</a><a href="#">Categories</a><a href="#">NewFatwas</a><a href="#">About</a><a href="#">Articles &amp; Books</a><a href="#">Send A Question</a><a href="#">Introduction to Islam</a>
  </nav>
  <div class="abs search">Search Key Word
    <span class="adv"><svg width="18" height="18" viewBox="0 0 18 18"><circle cx="7.5" cy="7.5" r="5.5" fill="none" stroke="#0a5a8c" stroke-width="2"/><line x1="11.5" y1="11.5" x2="16" y2="16" stroke="#0a5a8c" stroke-width="2.4" stroke-linecap="round"/></svg>Advance Search</span>
  </div>

  <section class="abs box intro">
    <div class="box-head">Introduction</div>
    <p>Welcome to Tolvene Hub Question &amp; Answer! This site aims to provide intelligent, authoritative responses to anyones question about Islam, whether it be from a Muslim or a non-Muslim, and to help solve general and personal social problems. Responses are composed by Sheikh Harun Idris Al-Basri, a known Islamic lecturer and author. Questions about any topic are welcome, such as theology, worship, human and business relations, or social and personal issues.</p>
    <p>All questions and answers on this site have been prepared, approved, revised, edited, amended or annotated by Shaykh Harun Idris al-Basri, the supervisor of this site. <span class="more">Read more</span></p>
  </section>

  <section class="abs topics">
    <div class="tabs">
      <div class="tab">Counselling</div>
      <div class="tab">Basic Tenets<br>of Faith</div>
      <div class="tab active">Contemporary<br>Transactions</div>
      <div class="tab">The Muslim<br>Woman</div>
      <div class="tab">Jurisprudence<br>Acts of Worship</div>
      <div class="tab">Jurisprudence of<br>Muslim Minorities</div>
    </div>
    <div class="tab-body">
      <ul class="topic-list">
        <li>Basic Tenets of Faith</li>
        <li>The Quraan and its Sciences.</li>
        <li>Hadeeth &amp; its Sciences</li>
        <li>Enjoining what is good and forbidding what is evil</li>
        <li>Psychological and Social Problems</li>
        <li>Islamic politics.</li>
        <li>Rulings on Jihaad.</li>
        <li class="current">Rulings on Jihaad.</li>
        <li>Rulings on Jihaad.</li>
      </ul>
      <div class="btn">READ MORE</div>
    </div>
  </section>

  <aside class="abs new-fatwas">
    <div class="box-head">New Fatwas</div>
    <div class="fatwa">He works as a nurse, which means that he may do some things that are not accept-able according to sharee’ah.</div>
    <div class="fatwa">He works as a nurse, which means that he may do some things that are not accept-able according to sharee’ah.</div>
    <div class="fatwa active">He works as a nurse, which means that he may do some things that are not accept-able according to sharee’ah.</div>
    <div class="fatwa">He works as a nurse, which means that he may do some things that are not accept-able according to sharee’ah.</div>
    <div class="fatwa">He works as a nurse, which means that he may do some things that are not accept-able according to sharee’ah.</div>
    <div class="fatwa" style="border:0">He works as a nurse, which means that he may do some things that are not accept-able according to sharee’ah.</div>
  </aside>

  <section class="abs col" style="left:33px">
    <div class="col-in">
      <h2>Categories</h2>
      <ul>
        <li>• <span class="linked">Basic Tenets of Faith.</span></li>
        <li>• The Quraan and its Sciences. •</li>
        <li style="padding-left:10px">Hadeeth &amp; its Sciences.</li>
        <li>• Rulings on Jihaad. • Fiqh of the family.</li>
        <li>• Islamic history and biography.</li>
        <li>• Enjoining what is good and forbidding</li>
      </ul>
    </div>
  </section>
  <section class="abs col" style="left:311px">
    <div class="col-in">
      <h2>File</h2>
      <ul>
        <li>• Basic Tenets of Faith.</li>
        <li>• The Quraan and its Sciences. •</li>
        <li>Hadeeth &amp; its Sciences.</li>
        <li>• Rulings on Jihaad. • Fiqh of the family.</li>
        <li>• Islamic history and biography.</li>
        <li>• Enjoining what is good and forbidding</li>
      </ul>
    </div>
  </section>
  <section class="abs col" style="left:589px">
    <div class="col-in">
      <h2>Latest Fatwas</h2>
      <ul>
        <li>• Basic Tenets of Faith.</li>
        <li>• The Quraan and its Sciences. •</li>
        <li>Hadeeth &amp; its Sciences.</li>
        <li>• Rulings on Jihaad. • Fiqh of the family.</li>
        <li>• Islamic history and biography.</li>
        <li>• Enjoining what is good and forbidding</li>
      </ul>
    </div>
  </section>
</body>
</html>
```